Kestrel Works Business Cards

This job is for the design of a business card.
I would like to review the design in 2x colour tones to choose from black and white inverted.
EG:
Black with white logo and white with black logo on BACK
White with black text on front and black with white text options
PRINTING DIMENSIONS: 4.5 x 8.5cm
Complete design will need to be provided in ready to print format with bleed lines
Target Market(s)
The audience of my business are people in the trade industry.
It will be also used for general networking with trades people and possible future clients.
I want to be represented as a professional, dynamic, creative and personable operator.
The card should reflect style, taste, experience, professionalism.
Industry/Entity Type
Business
Requirements
Must have
- BACK CONTENT:
- Logo in white and black background and vice versa with WHITE card and black logo review samples.
- FRONT CARD CONTENT:
- Name: Morgan Telvane
- Director
- Phone: 0438 216 947
- Email: morgan@kestrelworks.com.au
- Web: kestrelworks.com.au
- LICENCE #: KT-R 72158
Nice to have
- Possibly a textured background design on rear as a pose to a solid black
- Possibly adding a blue or orange discreet colour tone (possibly for email, phone abbreviated letter or symbols).

```html
<!DOCTYPE html>
<html lang="en">
<head>
<meta charset="UTF-8">
<title>Kestrel Works Business Cards</title>
<link rel="stylesheet" href="https://fonts.googleapis.com/css2?family=Open+Sans:wght@400&display=swap">
<style>
  :root {
    --page-bg: #dcd8d2;
    --charcoal: #262c30;
    --slate-light: #bfcbcb;
    --accent-orange: #f0401c;
    --text-light: #f2f4f4;
    --text-dark: #1d2326;
    --licence-grey: #9aa4a7;
  }
  * { box-sizing: border-box; margin: 0; padding: 0; }
  html, body {
    width: 1200px;
    height: 1000px;
    overflow: hidden;
    background: var(--page-bg);
    font-family: "Open Sans", sans-serif;
  }
  .card {
    position: absolute;
    left: 200px;
    width: 800px;
    height: 424px;
    overflow: hidden;
    box-shadow: 0 6px 18px rgba(0,0,0,0.18);
  }

  /* Logo side */
  .card-back {
    top: 56px;
    background: var(--charcoal);
  }
  .card-back .logo-band {
    position: absolute;
    left: 0;
    top: 136px;
    width: 710px;
    height: 144px;
    background: var(--slate-light);
  }
  .card-back .logo-band .accent-bar {
    position: absolute;
    right: 0;
    top: 0;
    width: 12px;
    height: 100%;
    background: var(--accent-orange);
    border-radius: 0 6px 6px 0;
  }
  .card-back .company-name {
    position: absolute;
    left: 0;
    width: 700px;
    top: 0;
    height: 144px;
    line-height: 144px;
    text-align: center;
    padding-left: 60px;
    font-size: 46px;
    letter-spacing: 2px;
    color: var(--text-dark);
  }
  .card-back .licence {
    position: absolute;
    left: 14px;
    bottom: 12px;
    font-size: 12px;
    letter-spacing: 0.5px;
    color: var(--licence-grey);
  }

  /* Details side */
  .card-front {
    top: 520px;
    background: var(--slate-light);
  }
  .card-front .edge-accent {
    position: absolute;
    left: 0;
    top: 96px;
    width: 6px;
    height: 84px;
    background: var(--accent-orange);
    border-radius: 0 4px 4px 0;
  }
  .card-front .person {
    position: absolute;
    left: 112px;
    top: 112px;
    color: var(--text-dark);
  }
  .card-front .person-name {
    font-size: 26px;
    line-height: 32px;
  }
  .card-front .person-role {
    font-size: 17px;
    line-height: 24px;
  }
  .card-front .logo-band {
    position: absolute;
    left: 352px;
    top: 60px;
    width: 448px;
    height: 120px;
    background: var(--charcoal);
  }
  .card-front .logo-band .accent-bar {
    position: absolute;
    left: 0;
    top: 0;
    width: 16px;
    height: 100%;
    background: var(--accent-orange);
    border-radius: 6px 0 0 6px;
  }
  .card-front .company-name {
    position: absolute;
    left: 16px;
    right: 0;
    top: 0;
    height: 120px;
    line-height: 120px;
    text-align: center;
    font-size: 36px;
    letter-spacing: 2px;
    color: var(--text-light);
  }
  .contact-list {
    position: absolute;
    left: 352px;
    top: 248px;
    list-style: none;
  }
  .contact-row {
    display: flex;
    height: 32px;
    margin-bottom: 12px;
    font-size: 19px;
    line-height: 32px;
  }
  .contact-label {
    background: var(--accent-orange);
    color: var(--text-light);
    padding: 0 8px;
  }
  .contact-value {
    background: var(--charcoal);
    color: var(--text-light);
    padding: 0 10px 0 6px;
  }
</style>
</head>
<body>
  <section class="card card-back" aria-label="Business card, logo side">
    <div class="logo-band">
      <div class="company-name">KESTREL WORKS</div>
      <div class="accent-bar"></div>
    </div>
    <p class="licence">LICENCE # KT-R 72158</p>
  </section>

  <section class="card card-front" aria-label="Business card, details side">
    <div class="edge-accent"></div>
    <div class="person">
      <p class="person-name">Morgan</p>
      <p class="person-role">Managing Director</p>
    </div>
    <div class="logo-band">
      <div class="accent-bar"></div>
      <div class="company-name">KESTREL WORKS</div>
    </div>
    <ul class="contact-list">
      <li class="contact-row"><span class="contact-label">MOBILE</span><span class="contact-value">0438216947</span></li>
      <li class="contact-row"><span class="contact-label">EMAIL</span><span class="contact-value">morgan@kestrelworks.com.au</span></li>
      <li class="contact-row"><span class="contact-label">WEB</span><span class="contact-value">kestrelworks.com.au</span></li>
    </ul>
  </section>
</body>
</html>
```